A taxi bidding business needs Web Design

We need a cutting edge, super UX-intuitive, Elegant web design for our business called Farovo.

Farovo is Australia based Kind of "Next Lyndo" business where user creates a trip and cabs/drivers place bids on fares/bookings/trips and lowest bidder gets the job.
User can also share the Cabs going in same route to get lowest bids.

- The design needs to be very, very intuitive to use and navigate. Please do not use much of yellow color.

References: StayMoor & Lyndo

Please see the attached pdf, attaching logo as well.

Target Market(s)

Ride Sharing, Taxi

Industry/Entity Type

Business

Number of Pages Required

5+ page

Requirements
Must have
• Icons/graphics, How it works icons, case studies icons, all mentioned pages
Should not have
• Not much yellow color

```html
<!DOCTYPE html>
<html lang="en">
<head>
<meta charset="utf-8">
<title>Farovo – Manage Bank Account</title>
<link rel="stylesheet" href="https://fonts.googleapis.com/css2?family=Exo+2:wght@500;600;700;800&family=Open+Sans:wght@400;600&display=swap">
<style>
  :root {
    --ink: #2b2b2b;
    --navy: #1f2a52;
    --banner: rgba(49, 60, 108, 0.88);
    --red: #d2232a;
    --line: #e1e1e1;
    --field-line: #dcdcdc;
    --muted: #8a8a8a;
    --page: #f8f8f8;
    --footer: #1d1c1b;
    --gold: #f0b400;
    --white: #ffffff;
  }
  * { box-sizing: border-box; margin: 0; padding: 0; }
  html, body { width: 1041px; height: 1200px; overflow: hidden; }
  body { position: relative; background: var(--white); font-family: "Open Sans", sans-serif; color: var(--ink); }

  .site-header { position: absolute; left: 0; top: 0; width: 1041px; height: 93px; border-bottom: 1px solid var(--line); }
  .menu-toggle { position: absolute; left: 114px; top: 24px; width: 44px; height: 44px; border: 1px solid #c9c9c9; border-radius: 50%; }
  .menu-toggle span { position: absolute; left: 13px; width: 18px; height: 2px; background: var(--navy); }
  .brand { position: absolute; left: 186px; top: 34px; display: flex; align-items: center; gap: 6px; font-family: "Exo 2", sans-serif; font-weight: 700; font-size: 19px; letter-spacing: 1px; color: var(--ink); }
  .brand-dot { width: 12px; height: 12px; border-radius: 50%; background: var(--red); }
  .logout { position: absolute; left: 847px; top: 34px; display: flex; align-items: center; gap: 6px; font-size: 12px; color: #555; }
  .logout-icon { width: 27px; height: 27px; border: 1px solid #ccc; border-radius: 50%; display: flex; align-items: center; justify-content: center; }

  .main-nav { position: absolute; left: 0; top: 93px; width: 1041px; height: 48px; }
  .main-nav a { position: absolute; top: 16px; font-family: "Exo 2", sans-serif; font-weight: 600; font-size: 11.5px; color: #3a3a3a; text-decoration: none; }
  .main-nav a.is-active { color: var(--navy); font-weight: 700; }

  .hero { position: absolute; left: 0; top: 141px; width: 1041px; height: 308px; background: linear-gradient(100deg, #d9d6d1 0%, #b8aca1 30%, #8f8a86 48%, #e6e7e8 70%, #cfd2d4 100%); }
  .hero-title { position: absolute; left: 346px; top: 119px; width: 580px; height: 71px; background: var(--banner); color: var(--white); font-family: "Exo 2", sans-serif; font-weight: 800; font-size: 42px; letter-spacing: 0.5px; display: flex; align-items: center; justify-content: center; }
  .hero-dots { position: absolute; left: 858px; top: 274px; display: flex; gap: 16px; }
  .hero-dots span { width: 12px; height: 12px; border: 2px solid var(--white); border-radius: 50%; }
  .hero-dots span.is-current { background: var(--gold); border-color: var(--gold); }

  .content { position: absolute; left: 0; top: 449px; width: 1041px; height: 553px; background: var(--page); }
  .bank-card { position: absolute; left: 114px; top: 108px; width: 812px; height: 352px; background: var(--white); border: 1px solid var(--line); }
  .avatar { position: absolute; left: 490px; top: 80px; width: 70px; height: 70px; border-radius: 50%; background: linear-gradient(160deg, #dfe7ef, #a9b8c8); border: 3px solid var(--white); box-shadow: 0 0 0 1px #d6d6d6; }
  .avatar-add { position: absolute; left: 552px; top: 541px; width: 11px; height: 11px; border-radius: 50%; background: var(--red); color: var(--white); font-size: 10px; line-height: 11px; text-align: center; font-weight: 700; }
  .field { position: absolute; left: 18px; width: 776px; height: 30px; border: 1px solid var(--field-line); display: flex; align-items: center; justify-content: space-between; padding: 0 12px; font-size: 9.5px; color: var(--muted); }
  .field svg { fill: #888; }
  .btn-update { position: absolute; left: 353px; top: 272px; width: 106px; height: 30px; border-radius: 15px; background: var(--red); color: var(--white); font-family: "Exo 2", sans-serif; font-weight: 700; font-size: 10px; display: flex; align-items: center; justify-content: center; }

  .site-footer { position: absolute; left: 0; top: 1002px; width: 1041px; height: 198px; background: linear-gradient(180deg, #262523, var(--footer)); border-top: 3px solid var(--gold); color: var(--white); font-size: 11px; }
  .footer-brand { position: absolute; left: 114px; top: 58px; display: flex; align-items: center; gap: 6px; font-family: "Exo 2", sans-serif; font-weight: 700; font-size: 22px; letter-spacing: 1px; }
  .footer-brand .brand-dot { background: var(--white); }
  .footer-help { position: absolute; left: 294px; top: 38px; display: flex; align-items: center; gap: 5px; }
  .footer-social { position: absolute; left: 294px; top: 106px; display: flex; gap: 8px; }
  .footer-social span { width: 8px; height: 8px; border-radius: 50%; background: var(--white); }
  .footer-links { position: absolute; left: 437px; top: 38px; list-style: none; line-height: 17px; }
  .footer-cities-title { position: absolute; left: 581px; top: 38px; color: var(--gold); }
  .footer-cities { position: absolute; top: 59px; list-style: none; line-height: 17px; }
  .store-badge { position: absolute; left: 825px; width: 100px; height: 33px; border: 1px solid #bbb; border-radius: 4px; background: #0d0d0d; }
  .footer-rule { position: absolute; left: 114px; top: 150px; width: 812px; height: 1px; background: #3a3937; }
  .copyright { position: absolute; left: 0; top: 167px; width: 1041px; text-align: center; font-size: 11px; }
</style>
</head>
<body>
  <header class="site-header">
    <div class="menu-toggle"><span style="top:15px"></span><span style="top:21px"></span><span style="top:27px"></span></div>
    <div class="brand"><span class="brand-dot"></span>Farovo</div>
    <div class="logout">
      <span class="logout-icon">
        <svg width="10" height="10" viewBox="0 0 10 10"><circle cx="5" cy="3" r="2.3" fill="#d2232a"/><path d="M1 10c0-3 1.8-4.3 4-4.3S9 7 9 10z" fill="#d2232a"/></svg>
      </span>LOG OUT
    </div>
  </header>

  <nav class="main-nav">
    <a style="left:116px">Profile</a>
    <a style="left:182px">Past Trip</a>
    <a style="left:264px">Manage Documents</a>
    <a class="is-active" style="left:399px">Manage Bank account</a>
    <a style="left:548px">Manage Vehicle</a>
    <a style="left:661px">Past Trips</a>
    <a style="left:749px">Earnings</a>
    <a style="left:827px">Invoices</a>
    <a style="left:901px">Help</a>
  </nav>

  <section class="hero" role="img" aria-label="Smiling driver at the wheel of a car, looking back over his shoulder">
    <h1 class="hero-title">MANAGE BANK ACCOUNT</h1>
    <div class="hero-dots"><span></span><span class="is-current"></span><span></span></div>
  </section>

  <main class="content">
    <div class="bank-card">
      <div class="field" style="top:77px">Add Bank Account Number
        <svg width="11" height="10" viewBox="0 0 11 10"><path d="M5.5 0L11 3H0z"/><rect x="1" y="4" width="1.6" height="4"/><rect x="4.7" y="4" width="1.6" height="4"/><rect x="8.4" y="4" width="1.6" height="4"/><rect x="0" y="8.5" width="11" height="1.5"/></svg>
      </div>
      <div class="field" style="top:138px">Account Name
        <svg width="9" height="10" viewBox="0 0 9 10"><circle cx="4.5" cy="2.7" r="2.5"/><path d="M0 10c0-3 2-4.5 4.5-4.5S9 7 9 10z"/></svg>
      </div>
      <div class="field" style="top:199px">BSB
        <svg width="10" height="10" viewBox="0 0 10 10"><circle cx="5" cy="5" r="3.6"/><circle cx="5" cy="5" r="1.4" fill="#fff"/><rect x="4.1" y="0" width="1.8" height="10"/><rect x="0" y="4.1" width="10" height="1.8"/></svg>
      </div>
      <div class="btn-update">Update</div>
    </div>
  </main>
  <div class="avatar" style="top:529px" role="img" aria-label="Driver profile photo"></div>
  <div class="avatar-add">+</div>

  <footer class="site-footer">
    <div class="footer-brand"><span class="brand-dot"></span>Farovo</div>
    <div class="footer-help">
      <svg width="11" height="11" viewBox="0 0 11 11"><circle cx="5.5" cy="5.5" r="4.5" fill="none" stroke="#fff" stroke-width="1.5"/><circle cx="5.5" cy="5.5" r="2" fill="none" stroke="#fff" stroke-width="1.2"/></svg>Help
    </div>
    <div class="footer-social"><span></span><span></span><span></span><span></span></div>
    <ul class="footer-links">
      <li>Ride</li><li>Drive</li><li>Cities</li><li>Fare Estimate</li><li>How It Works</li>
    </ul>
    <div class="footer-cities-title">TOP CITIES</div>
    <ul class="footer-cities" style="left:581px">
      <li>San Francisco</li><li>London</li><li>los Angels</li><li>Washington</li>
    </ul>
    <ul class="footer-cities" style="left:671px">
      <li>Washington D.C</li><li>Mexico City</li>
    </ul>
    <div class="store-badge" style="top:41px"></div>
    <div class="store-badge" style="top:76px"></div>
    <div class="footer-rule"></div>
    <p class="copyright">Copyrights © Farovo . 2017 | Allrights Reserved.</p>
  </footer>
</body>
</html>
```